Land Buying Company Needs Letterhead for Direct Mail Marketing to Land Owners

We are looking for a professional letterhead that we will be including in our direct mail marketing. We will be sending this to land owners who may be interested in selling or purchasing land.

The letterhead needs to be editable. Headers and footers would look nice, but we are open. We would want it to include our address, website, phone, and email info. For right now the address to use for design purposes would the following:

Address: 415 Bramwell Avenue #600
Dallas, TX 75219
Website - www.quillridgeacres.example
Email - info@quillridgeacres.example
Phone - 866-402-ACRE

I have attached our logo zip file that we just had done on Pixel Guild. Let me know what questions you have, and thank you.

```html
<!DOCTYPE html>
<html lang="en">
<head>
<meta charset="utf-8">
<title>Quill Ridge Acres Letterhead</title>
<link href="https://fonts.googleapis.com/css2?family=Montserrat:wght@400;500;700&display=swap" rel="stylesheet">
<style>
  :root {
    --canvas: #ece9e4;
    --paper: #ffffff;
    --lime: #8dbb3a;
    --olive: #4b5d22;
    --ink: #2b2b2b;
    --muted: #555555;
    --seal: #d9d9d9;
  }
  * { box-sizing: border-box; margin: 0; padding: 0; }
  html, body {
    width: 1200px; height: 800px; overflow: hidden;
    background: var(--canvas);
    font-family: "Montserrat", sans-serif;
  }
  .letterhead {
    position: absolute; left: 310px; top: 25px;
    width: 580px; height: 750px;
    background: var(--paper);
    box-shadow: 0 4px 18px rgba(0,0,0,0.12);
    color: var(--ink);
  }
  .header { position: absolute; left: 60px; right: 60px; top: 38px; }
  .brand { display: flex; align-items: center; justify-content: flex-end; gap: 10px; padding-right: 40px; }
  .brand-mark { width: 34px; height: 34px; border-radius: 50%; background: var(--olive); }
  .brand-name { font-weight: 700; font-size: 20px; letter-spacing: 1.5px; color: var(--lime); }
  .header-address { text-align: right; padding-right: 40px; margin-top: 6px; font-size: 7.5px; font-weight: 500; }
  .header-rule { margin-top: 12px; height: 1px; background: var(--lime); }

  .seal {
    position: absolute; left: 250px; top: 300px;
    width: 84px; height: 84px; border-radius: 50%;
    background: var(--seal); opacity: 0.55;
  }

  .body { position: absolute; left: 80px; right: 80px; top: 150px; font-size: 7.6px; line-height: 2; color: var(--muted); }
  .body p { margin-bottom: 12px; }
  .date, .recipient { margin-bottom: 14px; }
  .closing { margin-top: 20px; margin-bottom: 34px; }
  .signature { line-height: 1.7; }

  .footer { position: absolute; left: 60px; right: 60px; top: 658px; }
  .footer-name { text-align: center; font-weight: 700; font-size: 10px; letter-spacing: 0.6px; color: var(--olive); }
  .footer-rule { margin-top: 8px; height: 1px; background: var(--lime); }
  .contacts { display: flex; justify-content: space-between; margin-top: 7px; font-size: 7.5px; font-weight: 500; padding: 0 10px; }
  .contact { display: flex; align-items: center; gap: 4px; }
  .contact-dot { width: 5px; height: 5px; border-radius: 50%; background: var(--lime); }
</style>
</head>
<body>
  <main class="letterhead">
    <header class="header">
      <div class="brand">
        <span class="brand-mark"></span>
        <span class="brand-name">QUILL RIDGE ACRES</span>
      </div>
      <div class="header-address">415 Bramwell Avenue #600, Dallas, TX 75219</div>
      <div class="header-rule"></div>
    </header>

    <div class="seal"></div>

    <section class="body">
      <div class="date">August 10th, 2022</div>
      <div class="recipient">Full Last Name<br>Street Address<br>City, State 00000</div>
      <p>This is a sample letter that has been placed to demonstrate typing format for your company letterhead design. When positioned properly, it will serve to work in harmony with all other elements letterhead. This letterhead design is meant to project an image.</p>
      <p>The letterhead design is meant to project an image of professionalism and reliability. By using simple aligned shapes we have created a very spacious feeling. The simplicity suggests strength while the spaciousness contributes to the aesthetics of the layout.</p>
      <p>Look and feel reinforce the company brand. Letterhead design is meant to project an image of stability. When positioned properly, it will serve to work in harmony with all the other elements of the letterhead.</p>
      <p>This letterhead design is based on the form of your logo and your company mark. Each stationery piece carries a very spacious feeling. The simplicity suggests strength and spaciousness contributes to the form.</p>
      <p>Every piece of this stationery follows the same calm grid and spacing. The simplicity suggests strength and the spaciousness contributes to part of the form of your logo.</p>
      <div class="closing">Sincerely,</div>
      <div class="signature">Jordan Avery<br>Account Representative<br>P.O. Box 000<br>Anywhere, ST 00000</div>
    </section>

    <footer class="footer">
      <div class="footer-name">QUILL RIDGE ACRES</div>
      <div class="footer-rule"></div>
      <div class="contacts">
        <span class="contact"><span class="contact-dot"></span>866-402-ACRE</span>
        <span class="contact"><span class="contact-dot"></span>info@quillridgeacres.example</span>
        <span class="contact"><span class="contact-dot"></span>www.quillridgeacres.example</span>
      </div>
    </footer>
  </main>
</body>
</html>
```